2016 new customer flyer for kovaro customers

We need a 2 Sided Flyer Design for our website bargains. This will be sent to every customer who orders from us my site is www.shopvela.example - I want a 2 sided flyer, Promoting products on our clearance page and also advertising our guaranteed next day delivery, All items are in stock with QTY showing, This is the actual stock amount in stock. We need the flyers to attract new customers from kovaro to our site, 1 side of the flyer is to include "thank you for buying from our kovaro site" and also please leave positive feedback - with a big 5STARS image. if there is any problems with your order please contact us on 0861 574 219 6 - or email us - sales@shopvela.example

Target Market(s)

New customers who order from our kovaro site

Font styles to use
Sans Serif

Requirements
Must have
• my site is www.shopvela.example - I want a 2 sided flyer, Promoting products on our clearance page and also advertising our guaranteed next day delivery, All items are in stock with QTY showing, This is the actual stock amount in stock. We need the flyers to attract new customers from kovaro to our site, 1 side of the flyer is to include "thank you for buying from our kovaro site" and also please leave positive feedback - with a big 5STARS image. if there is any problems with your order please contact us on 0861 574 219 6 - or email us - sales@shopvela.example
Nice to have
• I need a flash flyer that is eye catching enough to get those customers visiting our site, We have many items on our website - www.shopvela.example

```html
<!DOCTYPE html>
<html lang="en">
<head>
<meta charset="utf-8">
<title>ShopVela – New Customer Flyer</title>
<link rel="stylesheet" href="https://fonts.googleapis.com/css2?family=Roboto+Condensed:wght@300;400;700&family=Open+Sans:wght@400;600;700&display=swap">
<style>
  :root{
    --backdrop:#8e8e8e;
    --blue:#1e8fe0;
    --blue-light:#3aa8f0;
    --blue-dark:#0d6fc0;
    --yellow:#fbd83a;
    --yellow-deep:#f3c321;
    --ink:#2a2a2a;
    --navy:#2a2d33;
    --white:#ffffff;
    --red:#e3121b;
    --red-dark:#a80c12;
  }
  *{box-sizing:border-box;margin:0;padding:0}
  html,body{width:1200px;height:858px;overflow:hidden;background:var(--backdrop)}
  .canvas{position:relative;width:1200px;height:858px}
  .flyer{position:absolute;top:30px;width:570px;height:800px;overflow:hidden;
    background:radial-gradient(circle at 50% 60%,var(--blue-light) 0%,var(--blue) 55%,var(--blue-dark) 100%);
    box-shadow:0 4px 14px rgba(0,0,0,.45);
    font-family:"Open Sans",Arial,sans-serif}
  .flyer--front{left:20px}
  .flyer--back{left:611px}
  .photo{position:absolute;left:0;top:0;width:100%}
  .curve{position:absolute;left:0;width:100%}
  .abs{position:absolute}

  /* front */
  .front-photo{height:400px;background:linear-gradient(135deg,#c9d3e4 0%,#9fb1cf 45%,#e6d6c8 70%,#cbd7ea 100%)}
  .brand-box{left:146px;top:362px;width:280px;height:78px;background:var(--white);border-radius:12px;
    display:flex;align-items:center;justify-content:center}
  .brand-name{font-family:"Roboto Condensed",Arial,sans-serif;font-weight:700;font-size:46px;color:var(--blue-dark);letter-spacing:-.5px}
  .thanks{left:0;width:100%;top:454px;text-align:center;font-family:"Roboto Condensed",Arial,sans-serif;
    font-weight:700;font-size:63px;line-height:1;color:var(--yellow);letter-spacing:-.5px}
  .purchase{left:0;width:100%;top:526px;text-align:center;font-family:"Roboto Condensed",Arial,sans-serif;
    font-weight:300;font-size:48px;line-height:1;color:var(--white);letter-spacing:2px}
  .feedback-band{left:0;top:587px;width:100%;height:51px;background:linear-gradient(var(--yellow),var(--yellow-deep));
    display:flex;align-items:center;justify-content:center;font-family:"Roboto Condensed",Arial,sans-serif;
    font-weight:700;font-size:30px;color:var(--ink)}
  .stars{left:146px;top:638px;width:278px;height:70px;background:var(--white);border-radius:0 0 12px 12px;
    display:flex;align-items:center;justify-content:center;gap:14px}
  .footer{left:0;top:736px;width:555px;height:64px;background:var(--navy);border-radius:0 34px 0 0;
    display:flex;flex-direction:column;align-items:center;justify-content:center;gap:1px;font-size:11.5px;color:var(--white)}
  .footer .lead{color:var(--yellow)}
  .footer .lead b{color:var(--white);font-weight:600}
  .contact-line{display:flex;align-items:center;gap:6px}
  .contact-line svg{width:10px;height:10px}

  /* back */
  .back-photo{height:330px;background:linear-gradient(120deg,#e6c64a 0%,#d8b63a 38%,#6f8fb8 55%,#a7c08a 80%,#cdd7c2 100%)}
  .ribbon{left:203px;top:302px;width:165px;height:172px}
  .ribbon-text{left:203px;top:310px;width:165px;text-align:center;font-family:"Roboto Condensed",Arial,sans-serif;color:var(--white)}
  .ribbon-text .pct{font-weight:700;font-size:50px;line-height:1}
  .ribbon-text .disc{font-weight:700;font-size:26px;color:var(--yellow);line-height:1.1}
  .ribbon-text .new{font-weight:400;font-size:19px;line-height:1.2}
  .goto{left:0;width:100%;top:485px;text-align:center;font-family:"Roboto Condensed",Arial,sans-serif;
    font-weight:700;font-size:46px;line-height:1;color:var(--yellow)}
  .coupon{left:0;width:100%;top:542px;text-align:center;font-family:"Roboto Condensed",Arial,sans-serif;
    font-weight:700;font-size:23px;color:var(--white)}
  .stock-tag{left:0;top:596px;height:18px;padding:0 14px 0 20px;background:var(--yellow);border-radius:0 9px 9px 0;
    font-size:10px;font-weight:700;color:var(--ink);display:flex;align-items:center}
  .stock-note{left:18px;top:620px;font-size:10.5px;color:var(--white)}
  .brand-strip{left:0;top:644px;width:100%;height:58px;background:var(--white);
    display:grid;grid-template-columns:repeat(6,74px);grid-template-rows:1fr 1fr;align-items:center;padding:2px 12px 2px 18px;column-gap:0}
  .partner{font-family:"Roboto Condensed",Arial,sans-serif;font-weight:700;font-size:14px;text-align:left}
  .courier{left:468px;top:578px;width:92px;height:150px;border-radius:6px;
    background:linear-gradient(#d9b993 0%,#c79e74 45%,#2b58a8 70%,#1c3f86 100%)}
  .footer-back{left:0;top:720px;width:100%;height:80px;background:var(--navy);border-radius:40px 40px 0 0}
  .delivery{left:18px;top:735px;font-family:"Roboto Condensed",Arial,sans-serif;color:var(--white)}
  .delivery .big{font-weight:700;font-size:24px;color:var(--yellow);line-height:1.1}
  .delivery .small{font-size:15px}
  .truck{left:248px;top:738px;width:66px;height:44px}
  .contact-back{left:365px;top:740px;font-size:12.5px;color:var(--white);display:flex;flex-direction:column;gap:1px}
  .contact-back .contact-line svg{width:11px;height:11px}
</style>
</head>
<body>
<div class="canvas">

  <section class="flyer flyer--front">
    <div class="photo front-photo" role="img" aria-label="Photo of a hand holding a white card reading THANK YOU"></div>
    <svg class="curve" style="top:330px" width="570" height="90" viewBox="0 0 570 90" aria-hidden="true">
      <path d="M0 62 Q285 -10 570 58 L570 90 L0 90 Z" fill="#1e8fe0"/>
      <path d="M0 56 Q285 -18 570 52" fill="none" stroke="#2a2d33" stroke-width="6"/>
      <path d="M0 62 Q285 -10 570 58" fill="none" stroke="#fbd83a" stroke-width="5"/>
    </svg>
    <div class="abs brand-box"><span class="brand-name">ShopVela</span></div>
    <div class="abs thanks">THANK YOU FOR</div>
    <div class="abs purchase">YOUR PURCHASE</div>
    <div class="abs feedback-band">PLEASE LEAVE POSITIVE FEEDBACK</div>
    <div class="abs stars" aria-label="Five stars">
      <svg width="38" height="36" viewBox="0 0 24 23"><path d="M12 0l3.1 7.6 8.2.6-6.3 5.3 2 8L12 17.2 5 21.5l2-8L.7 8.2l8.2-.6z" fill="#e3121b"/></svg>
      <svg width="38" height="36" viewBox="0 0 24 23"><path d="M12 0l3.1 7.6 8.2.6-6.3 5.3 2 8L12 17.2 5 21.5l2-8L.7 8.2l8.2-.6z" fill="#e3121b"/></svg>
      <svg width="38" height="36" viewBox="0 0 24 23"><path d="M12 0l3.1 7.6 8.2.6-6.3 5.3 2 8L12 17.2 5 21.5l2-8L.7 8.2l8.2-.6z" fill="#e3121b"/></svg>
      <svg width="38" height="36" viewBox="0 0 24 23"><path d="M12 0l3.1 7.6 8.2.6-6.3 5.3 2 8L12 17.2 5 21.5l2-8L.7 8.2l8.2-.6z" fill="#e3121b"/></svg>
      <svg width="38" height="36" viewBox="0 0 24 23"><path d="M12 0l3.1 7.6 8.2.6-6.3 5.3 2 8L12 17.2 5 21.5l2-8L.7 8.2l8.2-.6z" fill="#e3121b"/></svg>
    </div>
    <div class="abs footer">
      <div class="lead">if there is any problems with your order please <b>contact us on 0861 574 219 6</b></div>
      <div class="contact-line"><svg viewBox="0 0 10 10"><rect x=".5" y="1.5" width="9" height="7" fill="#fbd83a"/><path d="M.5 1.5 5 5.5 9.5 1.5" fill="none" stroke="#2a2d33"/></svg>sales@shopvela.example</div>
      <div class="contact-line"><svg viewBox="0 0 10 10"><circle cx="5" cy="5" r="4.5" fill="#fbd83a"/><path d="M.5 5h9M5 .5v9" stroke="#2a2d33" stroke-width=".8"/></svg>www.shopvela.example</div>
    </div>
  </section>

  <section class="flyer flyer--back">
    <div class="photo back-photo" role="img" aria-label="Photo of a smiling courier carrying parcels in front of a yellow delivery van"></div>
    <svg class="curve" style="top:270px" width="570" height="80" viewBox="0 0 570 80" aria-hidden="true">
      <path d="M0 52 Q285 0 570 48 L570 80 L0 80 Z" fill="#1e8fe0"/>
      <path d="M0 46 Q285 -6 570 42" fill="none" stroke="#2a2d33" stroke-width="6"/>
      <path d="M0 52 Q285 0 570 48" fill="none" stroke="#fbd83a" stroke-width="5"/>
    </svg>
    <svg class="abs ribbon" viewBox="0 0 165 172" aria-hidden="true">
      <defs><linearGradient id="rib" x1="0" y1="0" x2="0" y2="1"><stop offset="0" stop-color="#e3121b"/><stop offset="1" stop-color="#a80c12"/></linearGradient></defs>
      <path d="M0 0H165V172L82.5 135 0 172Z" fill="url(#rib)"/>
    </svg>
    <div class="abs ribbon-text">
      <div class="pct">10%</div>
      <div class="disc">DISCOUNT</div>
      <div class="new">ON NEW ORDERS</div>
    </div>
    <div class="abs goto">Go to www.ShopVela.example</div>
    <div class="abs coupon">and use this cupon code&nbsp; NEWC10 for discount</div>
    <div class="abs stock-tag">LIVE STOCK FIGURES</div>
    <div class="abs stock-note">We only sell what we have available for next day delivery.</div>
    <div class="abs brand-strip">
      <span class="partner" style="color:#1e8fe0">ShopVela</span>
      <span class="partner" style="color:#333">Starline</span>
      <span class="partner" style="color:#f3c321">bricko</span>
      <span class="partner" style="color:#333">novara</span>
      <span class="partner" style="color:#333">VOLTEX</span>
      <span class="partner" style="color:#e3121b">HEROIX</span>
      <span class="partner" style="color:#333">tonic</span>
      <span class="partner" style="color:#2f9a3a">powerly</span>
      <span class="partner" style="color:#333">sonara</span>
      <span class="partner" style="color:#1e8fe0">Tripgo</span>
      <span class="partner" style="color:#0d6fc0">Frostine</span>
      <span class="partner" style="color:#222">GALAXA</span>
    </div>
    <div class="abs courier" role="img" aria-label="Cut-out photo of a courier holding a stack of boxes"></div>
    <div class="abs footer-back"></div>
    <div class="abs delivery">
      <div class="big">Next Day Delivery</div>
      <div class="small">on orders placed before 12pm</div>
    </div>
    <svg class="abs truck" viewBox="0 0 66 44" aria-hidden="true">
      <rect x="2" y="4" width="38" height="28" rx="3" fill="#3aa8f0"/>
      <path d="M42 12h12l10 11v9H42z" fill="#3aa8f0"/>
      <circle cx="15" cy="35" r="7" fill="#3aa8f0" stroke="#2a2d33" stroke-width="3"/>
      <circle cx="52" cy="35" r="7" fill="#3aa8f0" stroke="#2a2d33" stroke-width="3"/>
    </svg>
    <div class="abs contact-back">
      <div class="contact-line"><svg viewBox="0 0 10 10"><path d="M2 .5 4 3 3 4.2C3.6 5.6 4.5 6.5 5.8 7L7 6l2.5 2L8.3 9.5C4.5 9.2 .8 5.5.5 1.7z" fill="#fbd83a"/></svg>0861 574 219 6</div>
      <div class="contact-line"><svg viewBox="0 0 10 10"><rect x=".5" y="1.5" width="9" height="7" fill="#fbd83a"/><path d="M.5 1.5 5 5.5 9.5 1.5" fill="none" stroke="#2a2d33"/></svg>sales@shopvela.example</div>
      <div class="contact-line"><svg viewBox="0 0 10 10"><circle cx="5" cy="5" r="4.5" fill="#fbd83a"/><path d="M.5 5h9M5 .5v9" stroke="#2a2d33" stroke-width=".8"/></svg>www.shopvela.example</div>
    </div>
  </section>

</div>
</body>
</html>
```